Moravel Stenwick Inc needs a business card design

Looking for a unique, classy and sharp business card design.

Contact Information for Business Card

Moravel Stenwick Inc.
Marisa Ortega Bellido BScOT(c)
Occupational Therapist
(780) 555-0142
moravelstenwick@postlynx.net

```html
<!DOCTYPE html>
<html lang="en">
<head>
<meta charset="utf-8">
<title>Moravel Stenwick Inc. — Business Card</title>
<link rel="stylesheet" href="https://fonts.googleapis.com/css2?family=Arimo:wght@400;500&display=swap">
<style>
  :root {
    --backdrop: #2b2b2b;
    --card: #ffffff;
    --purple: #92298f;
    --green: #8dc63f;
    --cyan: #2fb3e3;
    --ink: #1f1f1f;
    --rule: #3a3a3a;
  }
  * { margin: 0; padding: 0; box-sizing: border-box; }
  html, body {
    width: 1200px; height: 833px; overflow: hidden;
    background: var(--backdrop);
    font-family: "Arimo", Arial, sans-serif;
  }
  .canvas {
    position: relative; width: 1200px; height: 833px;
    display: flex; align-items: center; justify-content: center;
  }
  .card {
    position: relative; width: 1000px; height: 572px;
    background: var(--card); overflow: hidden;
  }
  .brand {
    position: absolute; left: 60px; top: 170px; width: 360px;
    display: flex; align-items: center; gap: 14px;
  }
  .brand-dot {
    width: 40px; height: 40px; border-radius: 50%;
    background: var(--green); flex: none;
  }
  .brand-name {
    font-size: 34px; font-weight: 500; color: var(--purple);
    line-height: 1.1;
  }
  .divider {
    position: absolute; left: 495px; top: 45px;
    width: 3px; height: 320px; background: var(--rule);
  }
  .contact {
    position: absolute; left: 545px; top: 95px;
  }
  .person-name {
    font-size: 27px; font-weight: 400; color: var(--purple);
  }
  .person-title {
    margin-top: 6px; font-size: 21px; color: var(--cyan);
  }
  .contact-list { list-style: none; margin-top: 52px; }
  .contact-item {
    display: flex; align-items: center; gap: 14px;
    font-size: 23px; color: var(--ink); margin-bottom: 12px;
  }
  .contact-icon { width: 22px; height: 22px; flex: none; }
  .swoosh {
    position: absolute; left: 0; bottom: 0; width: 1000px; height: 572px;
  }
</style>
</head>
<body>
<main class="canvas">
  <section class="card">
    <svg class="swoosh" viewBox="0 0 1000 572" aria-hidden="true">
      <path d="M0 378 Q430 300 900 450 Q430 335 0 408 Z" fill="var(--green)"/>
      <path d="M0 425 Q470 338 1000 490 L1000 572 L0 572 Z" fill="var(--purple)"/>
    </svg>

    <div class="brand">
      <span class="brand-dot"></span>
      <span class="brand-name">Moravel Stenwick Inc.</span>
    </div>

    <div class="divider"></div>

    <div class="contact">
      <p class="person-name">Marisa Ortega Bellido BScOT(c)</p>
      <p class="person-title">Occupational Therapist</p>
      <ul class="contact-list">
        <li class="contact-item">
          <svg class="contact-icon" viewBox="0 0 22 22" aria-hidden="true">
            <rect width="22" height="22" fill="var(--green)"/>
            <path d="M7 5 L9.5 5 L10.5 8.5 L9 9.7 Q10.5 12.8 12.6 13.6 L13.8 12.2 L17 13.3 L17 15.8 Q16 17 14 16.8 Q6.5 14.5 5.3 7 Q5.5 5.3 7 5 Z" fill="#fff"/>
          </svg>
          <span>(780) 555-0142</span>
        </li>
        <li class="contact-item">
          <svg class="contact-icon" viewBox="0 0 22 22" aria-hidden="true">
            <rect width="22" height="22" fill="var(--green)"/>
            <rect x="4" y="6" width="14" height="10" fill="none" stroke="#fff" stroke-width="1.6"/>
            <path d="M4 6 L11 12 L18 6" fill="none" stroke="#fff" stroke-width="1.6"/>
          </svg>
          <span>moravelstenwick@postlynx.net</span>
        </li>
      </ul>
    </div>
  </section>
</main>
</body>
</html>
```